Security Cheat Sheets

We are after a nicely presented easy to follow cheat sheet around security such as Phishing and scams and acceptable use we can send to our clients for awareness.
The example Cheat Sheets is some info we would like (was something i downloaded from the internet so do not copy verbatim but has some good content ideas we would like to use) and a very simple example i prepared plus our logos etc.

```html
<!DOCTYPE html>
<html lang="en">
<head>
<meta charset="utf-8">
<title>Phishing and Scams Cheat Sheet</title>
<link href="https://fonts.googleapis.com/css2?family=Oswald:wght@500;700&family=Open+Sans:wght@400;600&display=swap" rel="stylesheet">
<style>
:root{
  --blue:#1a3cc2;
  --blue-deep:#12299a;
  --lime:#6ee019;
  --lime-soft:#8bec3f;
  --white:#ffffff;
  --ink:#1b2440;
  --stage:#f1f2f4;
}
*{box-sizing:border-box;margin:0;padding:0}
html,body{width:1200px;height:2332px;overflow:hidden;background:var(--stage)}
body{position:relative;font-family:"Open Sans",Arial,sans-serif;color:var(--ink)}
.page{position:absolute;width:536px;height:768px;background:var(--white);box-shadow:0 4px 18px rgba(20,30,70,.14);overflow:hidden}
.p1{left:60px;top:32px}.p2{left:612px;top:32px}.p3{left:60px;top:852px}.p4{left:612px;top:852px}
.abs{position:absolute}
.h{font-family:"Oswald",Impact,sans-serif;font-weight:700;text-transform:uppercase;line-height:1.02}
.body{font-size:10.5px;line-height:1.55}
.on-blue{color:var(--white)}
.lime-t{color:var(--lime)}
.blue-t{color:var(--blue)}
.art{position:absolute;border-radius:6px}

/* page 1 */
.brand{left:30px;top:34px;display:flex;align-items:center;gap:10px}
.brand-dot{width:26px;height:26px;border-radius:50%;background:var(--blue)}
.brand-name{font-family:"Oswald",sans-serif;font-weight:500;font-size:20px;color:var(--blue);letter-spacing:.5px;line-height:1}
.title{left:30px;top:108px;font-size:50px;color:var(--blue)}
.title .lime-t{display:block}
.sheet-tag{left:300px;top:108px;width:112px;background:var(--lime);color:var(--white);font-size:40px;padding:8px 10px}
.monitor{left:30px;top:300px;width:300px;height:440px;background:var(--blue);padding:24px 22px}
.monitor .h{font-size:26px;margin-bottom:14px}
.cols{display:flex;gap:14px;margin-top:40px}
.cols > div{flex:1}
.cols .h{font-size:13px;margin-bottom:6px}
.cols p{font-size:9.5px;line-height:1.5}

/* page 2 */
.p2-title{left:28px;top:52px;font-size:32px;width:240px}
.cls{position:absolute;padding:16px 18px}
.cls .h{font-size:20px;margin-bottom:10px}
.cls-1{left:28px;top:180px;width:230px;height:200px;background:var(--lime)}
.cls-2{left:276px;top:220px;width:232px;height:160px;background:var(--blue)}
.cls-3{left:28px;top:398px;width:230px;height:170px;background:var(--blue)}
.defs{left:276px;top:398px;width:232px;height:340px;background:var(--lime);padding:20px 18px}
.defs .h.big{font-size:28px;margin-bottom:14px}
.defs .h.sub{font-size:14px;margin:12px 0 6px}
.p2-band{left:28px;top:586px;width:230px;height:152px;background:var(--blue-deep)}

/* page 3 */
.p3-left{left:0;top:0;width:258px;height:768px;background:var(--blue);padding:40px 26px}
.p3-left .h{font-size:30px;margin-bottom:14px}
.p3-left .h.second{margin-top:34px}
.p3-right{left:282px;top:40px;width:228px}
.p3-right .h{font-size:24px}
.p3-right .h.small{font-size:15px;margin:2px 0 12px}
.p3-right .h.gap{margin-top:34px;margin-bottom:12px}
.p3-foot{left:258px;top:700px;width:278px;height:68px;background:var(--lime)}

/* page 4 */
.p4-title{left:28px;top:40px;width:256px;font-size:28px}
.tile{position:absolute;padding:16px 18px}
.tile .h{font-size:24px;margin-bottom:10px}
.smish{left:300px;top:40px;width:208px;height:210px;background:var(--lime)}
.vish{left:300px;top:270px;width:208px;height:170px;background:var(--blue)}
.reset{left:300px;top:460px;width:208px;height:150px;background:var(--blue)}
.phish{left:28px;top:420px;width:252px;height:190px;background:var(--lime)}
.spear{left:28px;top:630px;width:252px;height:110px;background:var(--blue)}
.p4-foot{left:300px;top:630px;width:208px;height:110px;background:var(--lime-soft)}
</style>
</head>
<body>

<section class="page p1">
  <div class="abs brand">
    <div class="brand-dot"></div>
    <div class="brand-name">CORVANE</div>
  </div>
  <h1 class="abs h title">Phishing<span class="lime-t">and scams</span></h1>
  <div class="abs h sheet-tag">Cheat sheet</div>
  <div class="art" role="img" aria-label="Illustration of a security shield with circuit lines" style="left:340px;top:250px;width:170px;height:260px;background:radial-gradient(circle at 50% 45%,#7fe63a 0%,#2d6fd6 55%,#e9f0ff 100%)"></div>
  <div class="abs monitor">
    <h2 class="h lime-t">What's being monitored?</h2>
    <p class="body on-blue">Stay alert to unexpected messages asking for passwords, payments or urgent action. Check the sender, hover over links and report anything unusual to your IT team.</p>
    <div class="cols">
      <div><h3 class="h lime-t">Email</h3><p class="on-blue">Email traffic and attachments reviewed.</p></div>
      <div><h3 class="h lime-t">Web</h3><p class="on-blue">Web browsing on company devices.</p></div>
      <div><h3 class="h lime-t">Access</h3><p class="on-blue">Remote access and login activity.</p></div>
    </div>
  </div>
</section>

<section class="page p2">
  <h1 class="abs h p2-title blue-t">Data classification <span class="lime-t">and handling</span></h1>
  <div class="art" role="img" aria-label="Illustration of a padlock, shield and laptop" style="left:300px;top:24px;width:208px;height:180px;background:linear-gradient(135deg,#b8f27d,#3b78e0)"></div>
  <div class="cls cls-1"><h2 class="h on-blue">Class 1<br>Highly confidential</h2><p class="body on-blue">Payroll, contracts, client secrets and passwords. Encrypt and share only with approved staff.</p></div>
  <div class="cls cls-2"><h2 class="h lime-t">Class 2<br>Confidential</h2><p class="body on-blue">Internal plans and reports. Keep inside the business.</p></div>
  <div class="cls cls-3"><h2 class="h lime-t">Class 3<br>Public</h2><p class="body on-blue">Marketing material and website content cleared for release.</p></div>
  <div class="abs defs">
    <h2 class="h big on-blue">Definitions</h2>
    <h3 class="h sub blue-t">Unidentified data</h3>
    <p class="body on-blue">Data that cannot be linked to any single person or client.</p>
    <h3 class="h sub blue-t">Aggregate data</h3>
    <p class="body on-blue">Combined figures that summarise many records without detail.</p>
  </div>
  <div class="abs p2-band"></div>
</section>

<section class="page p3">
  <div class="abs p3-left">
    <h2 class="h lime-t">Universal signs it's a scam</h2>
    <p class="body on-blue">Urgent tone, unexpected requests, spelling errors, mismatched sender addresses and links that do not match the text are all common warning signs.</p>
    <h2 class="h lime-t second">So I think I see scam &amp; scams, now what?</h2>
    <p class="body on-blue">Do not click or reply. Report the message, delete it and contact the sender through a known channel.</p>
  </div>
  <div class="abs p3-right">
    <h2 class="h lime-t">Random fact</h2>
    <h3 class="h small blue-t">Phishing through the ages</h3>
    <p class="body">Phishing dates back to the mid 1990s, when attackers posed as staff to steal account logins. The tactics have changed, the goal has not.</p>
    <h2 class="h gap lime-t">Video/online meeting scams</h2>
    <p class="body">Fake meeting invites can carry harmful links. Join only from your calendar and confirm unknown invites with the organiser.</p>
  </div>
  <div class="abs p3-foot"></div>
</section>

<section class="page p4">
  <h1 class="abs h p4-title blue-t">Phishing &amp; scams<br><span class="lime-t">what do I<br>look for?</span></h1>
  <div class="art" role="img" aria-label="Illustration of a worker at a laptop receiving suspicious messages" style="left:60px;top:200px;width:210px;height:200px;background:linear-gradient(160deg,#ffd9a8,#6ea6f0)"></div>
  <div class="tile smish"><h2 class="h on-blue">Smishing</h2><p class="body on-blue">Scam text messages with links or callback numbers.</p></div>
  <div class="tile vish"><h2 class="h lime-t">Vishing</h2><p class="body on-blue">Phone calls from fake support or banks asking for codes.</p></div>
  <div class="tile reset"><h2 class="h lime-t">Password reset scams</h2><p class="body on-blue">Fake reset notices that lead to look-alike login pages.</p></div>
  <div class="tile phish"><h2 class="h on-blue">Phishing</h2><p class="body on-blue">Emails pretending to be trusted senders that ask you to click, log in or pay.</p></div>
  <div class="tile spear"><h2 class="h lime-t">Spears &amp; whales?</h2><p class="body on-blue">Targeted attacks aimed at specific staff or senior leaders.</p></div>
  <div class="abs p4-foot"></div>
</section>

</body>
</html>
```